Brexmoor Solutions
Not Necessary
Simple
Marlon Teague
N/A
marlon@brexmoorsolutions.example
http://www.brexmoorsolutions.example
Brexmoor Solutions is a custom development/software development firm. Specialize on web and mobile development.
I'd be interested in what a double sided business card looks like but may settle on a one-sided card.
Your discretion on whether to use logo's font or another - whatever looks best.
Logo and fonts

```html
<!DOCTYPE html>
<html lang="en">
<head>
<meta charset="utf-8">
<title>Brexmoor Solutions — Business Card</title>
<link href="https://fonts.googleapis.com/css2?family=Raleway:wght@400;600;700&display=swap" rel="stylesheet">
<style>
  :root {
    --backdrop: #ecebe8;
    --card-white: #ffffff;
    --blue-deep: #0b4f8e;
    --blue-mid: #1a72c0;
    --blue-light: #3c9ae0;
    --ink: #2b3440;
    --ink-soft: #5a6673;
  }
  * { box-sizing: border-box; margin: 0; padding: 0; }
  html, body {
    width: 1200px; height: 739px; overflow: hidden;
    background: var(--backdrop);
    font-family: "Raleway", Arial, sans-serif;
  }
  .canvas {
    position: relative; width: 1200px; height: 739px;
    display: flex; align-items: center; justify-content: center; gap: 40px;
  }
  .card {
    position: relative; width: 540px; height: 309px; overflow: hidden;
    box-shadow: 0 10px 28px rgba(0,0,0,.18);
  }
  .card-back {
    background: radial-gradient(ellipse at 35% 40%, var(--blue-light) 0%, var(--blue-mid) 40%, var(--blue-deep) 100%);
  }
  .card-back .website {
    position: absolute; right: 34px; top: 40px;
    color: #ffffff; font-size: 15px; font-weight: 600; letter-spacing: 2.5px;
  }
  .card-front { background: var(--card-white); }
  .brand {
    position: absolute; left: 72px; top: 70px;
    display: flex; align-items: center; gap: 14px;
  }
  .brand-dot { width: 34px; height: 34px; border-radius: 50%; background: var(--blue-mid); }
  .brand-name {
    font-size: 38px; font-weight: 700; color: var(--blue-deep); letter-spacing: .5px;
  }
  .person-name {
    position: absolute; left: 300px; top: 140px;
    font-size: 21px; font-weight: 700; color: var(--blue-mid);
  }
  .contacts {
    position: absolute; left: 24px; right: 20px; bottom: 52px;
    display: flex; justify-content: space-between; align-items: center;
    font-size: 11px; color: var(--ink-soft);
  }
  .contact { display: flex; align-items: center; gap: 5px; }
  .contact svg { width: 13px; height: 13px; fill: var(--ink); }
  .band {
    position: absolute; left: 0; right: 0; bottom: 0; height: 32px;
    background: linear-gradient(90deg, var(--blue-deep), var(--blue-light) 50%, var(--blue-deep));
  }
  .band::before {
    content: ""; position: absolute; left: 0; right: 0; top: 0; height: 4px;
    background: var(--blue-light); opacity: .6;
  }
</style>
</head>
<body>
<main class="canvas">
  <section class="card card-back" aria-label="Card back">
    <p class="website">www.brexmoorsolutions.example</p>
  </section>

  <section class="card card-front" aria-label="Card front">
    <div class="brand">
      <span class="brand-dot"></span>
      <span class="brand-name">Brexmoor Solutions</span>
    </div>
    <p class="person-name">Marlon Teague</p>

    <div class="contacts">
      <span class="contact">
        <svg viewBox="0 0 16 16"><path d="M8 1 1 7.5h2V15h4v-4h2v4h4V7.5h2z"/></svg>N/A
      </span>
      <span class="contact">
        <svg viewBox="0 0 16 16"><path d="M4 1.5 6.3 4.8 5 6.4a9 9 0 0 0 4.6 4.6l1.6-1.3 3.3 2.3-1.3 2.5C7.6 14.5 1.5 8.4 1.5 2.8z"/></svg>555-014-2290
      </span>
      <span class="contact">
        <svg viewBox="0 0 16 16"><path d="M1 3h14v10H1zm1.2 1.2v.4L8 8.8l5.8-4.2v-.4zm0 1.9v5.7h11.6V6.1L8 10.3z"/></svg>marlon@brexmoorsolutions.example
      </span>
      <span class="contact">
        <svg viewBox="0 0 16 16"><path d="M8 1a7 7 0 1 0 0 14A7 7 0 0 0 8 1zm0 1.4c.8 0 1.8 1.6 2.1 4.1H5.9C6.2 4 7.2 2.4 8 2.4zm-5.5 4.1h2.2c.1-1.4.4-2.7.9-3.6A5.6 5.6 0 0 0 2.5 6.5zm0 1.4h2.2c.1 1.4.4 2.7.9 3.6a5.6 5.6 0 0 1-3.1-3.6zm3.4 0h4.2c-.3 2.5-1.3 4.1-2.1 4.1S6.2 10.4 5.9 7.9zm5.4 0h2.2a5.6 5.6 0 0 1-3.1 3.6c.5-.9.8-2.2.9-3.6zm0-1.4c-.1-1.4-.4-2.7-.9-3.6a5.6 5.6 0 0 1 3.1 3.6z"/></svg>brexmoorsolutions.example
      </span>
    </div>
    <div class="band"></div>
  </section>
</main>
</body>
</html>
```